Business cards / Letterheads / Compliment slips

We are looking to get business cards, letterheads and compliment slips designed.

These will all have to follow the design of our new website and logo. Links to the website, logo and fonts can be found below...

The designs need to be simple with focus on the typography. Only the following colours should be used on the designs...

#7f9d3c
#191818
#fff

Website:
http://brookfieldweb.examplestudio.co.uk/

Logo:
https://www.filecrate.example/sh/8kd2m4qwzpla7ve/hTr5NpQ2Xw/logos

Fonts:
https://www.filecrate.example/sh/8kd2m4qwzpla7ve/Q9vTzR3mKe/Fonts/BayerModern_TTF

and

https://www.filecrate.example/sh/8kd2m4qwzpla7ve/W7nHcY5pD3/Fonts/MuseoSansFamily

Reason: We would like some more design submissions

Reason: We are still deciding on designs we like and would like to see some more submissions...

Industry/Entity Type

Business

Requirements
Must have
• The designs need to be simple with focus on the typography. Only the following colours should be used on the designs...

#7f9d3c
#191818
#fff
Should not have
• - Any fonts that are not provided.
- Any colours that are not provided.

```html
<!DOCTYPE html>
<html lang="en">
<head>
<meta charset="utf-8">
<title>brookfieldweb stationery</title>
<link rel="stylesheet" href="https://fonts.googleapis.com/css2?family=Nunito+Sans:wght@400;600;700&display=swap">
<style>
  :root {
    --green: #7f9d3c;
    --ink: #191818;
    --paper: #fff;
    --muted: #d8d8d8;
    --backdrop: #f0f0f0;
    --shadow: 0 2px 6px rgba(0,0,0,.28);
  }
  * { margin: 0; padding: 0; box-sizing: border-box; }
  html, body { width: 1200px; height: 900px; overflow: hidden; }
  body {
    position: relative;
    background: var(--backdrop);
    font-family: "Nunito Sans", sans-serif;
    color: var(--ink);
  }
  .sheet {
    position: absolute;
    background: var(--paper);
    box-shadow: var(--shadow);
  }
  .brand {
    position: absolute;
    display: flex;
    align-items: center;
    color: var(--ink);
    font-weight: 700;
    letter-spacing: -0.02em;
  }
  .brand-dot {
    display: block;
    border-radius: 50%;
    background: var(--green);
    flex: none;
  }
  .green { color: var(--green); }
  .footer-band {
    position: absolute;
    left: 0; right: 0; bottom: 0;
    background: var(--ink);
  }
  .footer-band::before {
    content: "";
    position: absolute;
    left: 0; top: 0; bottom: 0;
    width: var(--accent-w);
    background: var(--green);
  }
  .address { position: absolute; line-height: 1.18; font-style: normal; }
  .address .office { color: var(--green); }
  .web { position: absolute; letter-spacing: 0.04em; }

  /* Letterhead */
  .letterhead { left: 75px; top: 30px; width: 595px; height: 840px; }
  .letterhead .brand { left: 35px; top: 37px; font-size: 24px; gap: 7px; }
  .letterhead .brand-dot { width: 40px; height: 40px; }
  .letterhead .address { right: 25px; top: 38px; text-align: right; font-size: 12.5px; }
  .letterhead .phone { font-size: 14.5px; color: var(--green); margin-top: 10px; display: block; }
  .letterhead .web { left: 0; right: 0; top: 797px; text-align: center; font-size: 12px; }
  .letterhead .footer-band { height: 23px; --accent-w: 44px; }

  /* Business card front */
  .card-front { left: 570px; top: 286px; width: 256px; height: 148px; }
  .card-front .brand { left: 18px; top: 14px; font-size: 13.5px; gap: 4px; }
  .card-front .brand-dot { width: 21px; height: 21px; }
  .card-front .person { position: absolute; right: 18px; top: 19px; text-align: right; }
  .card-front .person-name { font-size: 11px; font-weight: 700; color: var(--green); line-height: 1.1; }
  .card-front .person-role { font-size: 7.5px; line-height: 1.1; }
  .card-front .address { left: 18px; top: 57px; font-size: 7.5px; line-height: 1.25; }
  .card-front .phone { font-size: 10px; color: var(--green); margin-top: 6px; display: block; line-height: 1.1; }
  .card-front .web { right: 14px; top: 121px; font-size: 7.5px; letter-spacing: 0.02em; }
  .card-front .footer-band { height: 11px; --accent-w: 16px; }

  /* Business card back */
  .card-back { left: 845px; top: 289px; width: 254px; height: 144px; background: var(--ink); }
  .card-back .brand-dot { position: absolute; left: 93px; top: 22px; width: 62px; height: 62px; }
  .card-back .tagline {
    position: absolute; left: 0; right: 0; top: 105px;
    text-align: center; font-size: 9.5px; line-height: 1.3; color: var(--muted);
  }

  /* Compliment slip */
  .comp-slip { left: 503px; top: 482px; width: 596px; height: 282px; }
  .comp-slip .brand { left: 30px; top: 30px; font-size: 22px; gap: 6px; }
  .comp-slip .brand-dot { width: 38px; height: 38px; }
  .comp-slip .headline { position: absolute; right: 34px; top: 36px; font-size: 20px; font-weight: 400; color: var(--green); }
  .comp-slip .address { left: 32px; top: 139px; font-size: 12px; }
  .comp-slip .phone { font-size: 14.5px; color: var(--green); margin-top: 11px; display: block; }
  .comp-slip .web { right: 40px; top: 234px; font-size: 11.5px; }
  .comp-slip .footer-band { height: 24px; --accent-w: 27px; }
</style>
</head>
<body>

<section class="sheet letterhead" aria-label="Letterhead">
  <div class="brand"><span class="brand-dot"></span>brookfieldweb</div>
  <address class="address">
    <span class="office">Wexley Head Office</span><br>
    Floor 2,<br>18 Calder Row,<br>Wexley,<br>WX4 7QP
    <span class="phone">0854 611 3042</span>
    hello@brookfieldweb.co.uk
  </address>
  <p class="web">www.<span class="green">brookfieldweb</span>.co.uk</p>
  <div class="footer-band"></div>
</section>

<section class="sheet card-front" aria-label="Business card front">
  <div class="brand"><span class="brand-dot"></span>brookfieldweb</div>
  <div class="person">
    <p class="person-name">Owen Hartley</p>
    <p class="person-role">General manager</p>
  </div>
  <address class="address">
    <span class="office">Wexley Head Office</span><br>
    Floor 2,<br>18 Calder Row,<br>Wexley,<br>WX4 7QP
    <span class="phone">0854 611 3042</span>
    hello@brookfieldweb.co.uk
  </address>
  <p class="web">www.<span class="green">brookfieldweb</span>.co.uk</p>
  <div class="footer-band"></div>
</section>

<section class="sheet card-back" aria-label="Business card back">
  <span class="brand-dot"></span>
  <p class="tagline">We drive search led<br>growth for better <span class="green">returns</span></p>
</section>

<section class="sheet comp-slip" aria-label="Compliment slip">
  <div class="brand"><span class="brand-dot"></span>brookfieldweb</div>
  <h1 class="headline">With Compliments</h1>
  <address class="address">
    <span class="office">Wexley Head Office</span><br>
    Floor 2,<br>18 Calder Row,<br>Wexley,<br>WX4 7QP
    <span class="phone">0854 611 3042</span>
    hello@brookfieldweb.co.uk
  </address>
  <p class="web">www.<span class="green">brookfieldweb</span>.co.uk</p>
  <div class="footer-band"></div>
</section>

</body>
</html>
```